Brightmoor Vector Systems Website

I am starting an IT consulting business called Brightmoor Vector Systems. I recently completed a logo contest on ArtHive and am now looking to put together a basic website. I can provide text and content but am looking for a site design with layout and graphics. I am attaching my logo below. I was thinking of a dark blue and white theme for the website (similar to the logo). However, I am open to ideas. Graphics can be a mix of business and high tech as that is the image I am trying to convey. The site will be relatively simple and probably have only 3 - 5 pages (Home, About Us, Services, Contact, etc.)
Target Market(s)
United States commercial companies and government contractors
Industry/Entity Type
Consulting

```html
<!DOCTYPE html>
<html lang="en">
<head>
<meta charset="utf-8">
<title>Brightmoor Vector Systems</title>
<link rel="stylesheet" href="https://fonts.googleapis.com/css2?family=Roboto:wght@400;500;700;900&family=Poppins:wght@400;500;600;700&display=swap">
<style>
:root{
  --brand:#0b5aa8;
  --brand-bright:#0a6bcb;
  --page:#f5f5f5;
  --white:#ffffff;
  --ink:#222222;
  --muted:#777777;
  --dark:#2b2c31;
  --red:#e31e2c;
  --line:#dddddd;
}
*{margin:0;padding:0;box-sizing:border-box}
html,body{width:746px;height:1200px;overflow:hidden}
body{position:relative;background:var(--page);font-family:"Roboto",Arial,sans-serif;color:var(--ink)}
.abs{position:absolute}
.top-band{left:0;top:0;width:746px;height:70px;background:var(--brand)}
.navbar{left:55px;top:36px;width:653px;height:61px;background:var(--white)}
.brand{left:29px;top:22px;font-size:11px;font-weight:500;color:var(--ink);letter-spacing:.2px;display:flex;align-items:center;gap:5px}
.brand-dot{width:8px;height:8px;border-radius:50%;background:var(--brand)}
.brand small{display:block;font-size:4.2px;letter-spacing:2.4px;color:#444;margin-top:1px}
.nav-link{top:26px;font-size:10px;font-weight:700;color:var(--brand);letter-spacing:.2px}
.contact-bar{left:0;top:107px;width:746px;height:46px}
.divider{top:5px;width:1px;height:28px;background:var(--line)}
.c-label{font-size:9.5px;font-weight:700;color:var(--brand)}
.c-value{font-size:9.5px;color:#333;margin-top:3px}
.social{top:10px;width:21px;height:21px;border-radius:50%;background:var(--white);display:flex;align-items:center;justify-content:center}
.social span{width:4px;height:4px;border-radius:50%;background:#888}
.hero{left:0;top:153px;width:746px;height:289px;background:linear-gradient(100deg,#6f7b7f 0%,#d7cbb8 30%,#e8dccb 50%,#c9a27a 62%,#a8b9b4 80%,#7f9590 100%)}
.slide-arrow{top:153px;width:22px;height:54px;background:rgba(60,70,80,.45);display:flex;align-items:center;justify-content:center}
.to-top{left:710px;top:399px;width:31px;height:30px;background:var(--brand-bright);display:flex;align-items:center;justify-content:center}
.about-frame{left:47px;top:475px;width:218px;height:273px;background:#efefef}
.about-photo{left:79px;top:507px;width:218px;height:205px;background:linear-gradient(160deg,#5a5a58 0%,#8d8c86 45%,#3d3d3b 100%)}
.quote{top:733px;width:17px;height:15px;border-radius:50%;background:#e4e4e4}
.eyebrow{left:369px;top:473px;font-size:9.5px;font-weight:700;color:var(--brand)}
.about-title{left:368px;top:489px;font-size:26px;font-weight:900;color:var(--brand-bright);letter-spacing:.3px}
.about-text{left:367px;top:538px;width:300px;font-size:7.3px;line-height:9px;font-weight:500;color:var(--muted)}
.mission{left:366px;top:604px;width:303px;height:119px;background:var(--brand-bright)}
.mission-title{left:86px;top:21px;font-size:11px;font-weight:700;color:var(--white);text-decoration:underline}
.mission-sub{left:86px;top:49px;font-size:7.5px;font-weight:700;color:var(--white)}
.services{left:0;top:760px;width:746px;height:278px;background:var(--dark)}
.services-title{left:0;top:20px;width:746px;text-align:center;font-size:26px;font-weight:900;color:var(--white)}
.svc-photo{top:67px;width:182px;height:123px}
.svc-card{top:170px;width:162px;height:89px;background:var(--white);font-family:"Poppins",sans-serif}
.svc-icon-col{left:0;top:0;width:34px;height:89px;background:linear-gradient(#ffffff,#f0f0f0);display:flex;align-items:center;justify-content:center}
.svc-name{left:49px;top:13px;font-size:10.5px;font-weight:500;color:var(--ink)}
.svc-text{left:49px;top:36px;width:112px;font-size:6.9px;line-height:12.3px;color:var(--muted)}
.plus{width:25px;height:25px;border-radius:50%;background:var(--red);top:158px;display:flex;align-items:center;justify-content:center}
.clients-eyebrow{left:50px;top:1048px;font-family:"Poppins",sans-serif;font-size:7px;font-weight:500;color:var(--red)}
.clients-title{left:50px;top:1060px;font-family:"Poppins",sans-serif;font-size:18px;color:var(--ink)}
.clients-title b{font-weight:700}
.arrow-btn{top:1050px;width:29px;height:29px;border-radius:50%;border:1px solid #dcdcdc;display:flex;align-items:center;justify-content:center}
.client{top:1111px;width:90px;height:68px;background:var(--white);display:flex;align-items:center;justify-content:center;font-family:"Poppins",sans-serif;font-size:13px;font-weight:500;color:#cfcfcf}
</style>
</head>
<body>
<div class="abs top-band"></div>

<header class="abs navbar">
  <div class="abs brand"><span class="brand-dot"></span><div>BRIGHTMOOR VECTOR<small>SYSTEMS</small></div></div>
  <span class="abs nav-link" style="left:166px">HOME</span>
  <span class="abs nav-link" style="left:220px">ABOUT&nbsp; US</span>
  <span class="abs nav-link" style="left:303px">PRODUCTS</span>
  <span class="abs nav-link" style="left:381px">SERVICES</span>
  <span class="abs nav-link" style="left:456px">CONTACT US</span>
  <svg class="abs" style="left:547px;top:26px" width="12" height="12" viewBox="0 0 12 12"><circle cx="5" cy="5" r="3.6" fill="none" stroke="#0b5aa8" stroke-width="1.8"/><line x1="7.6" y1="7.6" x2="11" y2="11" stroke="#0b5aa8" stroke-width="2"/></svg>
</header>

<section class="abs contact-bar">
  <div class="abs divider" style="left:60px"></div>
  <svg class="abs" style="left:70px;top:6px" width="23" height="23" viewBox="0 0 24 24" fill="none" stroke="#b5b5b5" stroke-width="1"><circle cx="12" cy="12" r="11"/><ellipse cx="12" cy="12" rx="5" ry="11"/><line x1="1" y1="12" x2="23" y2="12"/></svg>
  <div class="abs" style="left:105px;top:8px"><div class="c-label">Address</div><div class="c-value">Elm St. 14 , USA</div></div>
  <div class="abs divider" style="left:252px"></div>
  <svg class="abs" style="left:264px;top:7px" width="22" height="22" viewBox="0 0 24 24" fill="none" stroke="#b5b5b5" stroke-width="1"><path d="M5 2l4 5-2 3c1 3 4 6 7 7l3-2 5 4-3 4C10 22 2 14 1 5z"/><path d="M14 4a6 6 0 0 1 6 6M14 7a3 3 0 0 1 3 3"/></svg>
  <div class="abs" style="left:298px;top:8px"><div class="c-label">Phone</div><div class="c-value">021-5550187</div></div>
  <div class="abs divider" style="left:402px"></div>
  <svg class="abs" style="left:414px;top:7px" width="22" height="22" viewBox="0 0 24 24" fill="none" stroke="#b5b5b5" stroke-width="1"><path d="M3 10l18-8-5 19-5-6z"/><path d="M21 2L11 15"/><path d="M1 18h6M1 21h8"/></svg>
  <div class="abs" style="left:448px;top:8px"><div class="c-label">Email</div><div class="c-value" style="margin-top:6px">info@brightmoorvector.com</div></div>
  <div class="abs divider" style="left:579px"></div>
  <div class="abs social" style="left:607px"><span></span></div>
  <div class="abs social" style="left:634px"><span></span></div>
  <div class="abs social" style="left:661px"><span></span></div>
</section>

<div class="abs hero" role="img" aria-label="Bright modern office reception with slatted wooden ceiling, orange lounge chairs and glass walls overlooking the city"></div>
<div class="abs slide-arrow" style="left:0"><svg width="7" height="11" viewBox="0 0 7 11"><path d="M6 1L1 5.5 6 10" fill="none" stroke="#fff" stroke-width="1.2"/></svg></div>
<div class="abs slide-arrow" style="left:727px;width:19px"><svg width="7" height="11" viewBox="0 0 7 11"><path d="M1 1l5 4.5L1 10" fill="none" stroke="#fff" stroke-width="1.2"/></svg></div>
<div class="abs to-top"><svg width="10" height="7" viewBox="0 0 10 7"><path d="M1 6l4-4 4 4" fill="none" stroke="#fff" stroke-width="1.6"/></svg></div>

<section>
  <div class="abs about-frame"></div>
  <div class="abs about-photo" role="img" aria-label="Minimal office with a white executive chair, glass desk and large industrial windows"></div>
  <div class="abs quote" style="left:207px"></div>
  <div class="abs quote" style="left:226px"></div>
  <div class="abs eyebrow">About Us</div>
  <h1 class="abs about-title">BRIGHTMOOR VECTOR</h1>
  <p class="abs about-text">Lorem ipsum dolor sit amet, consectetur adipiscing elit. Nullam dictum tempor mi, nec ornare orci interdum quis. Curabitur justo turpis, egestas vitae nunc a, porta tincidunt eros.</p>
  <div class="abs mission">
    <svg class="abs" style="left:20px;top:41px" width="50" height="46" viewBox="0 0 50 46" fill="none" stroke="#fff" stroke-width="2"><path d="M38 12A20 20 0 1 0 42 28" stroke-dasharray="60 4 3 4"/><circle cx="22" cy="23" r="12"/><circle cx="22" cy="23" r="5"/><path d="M22 23h20"/><path d="M40 17l7 2-3 4 3 4-7 2z"/></svg>
    <div class="abs mission-title">Mission</div>
    <div class="abs mission-sub">Mission Company</div>
  </div>
  <svg class="abs" style="left:387px;top:722px" width="17" height="18" viewBox="0 0 17 18"><path d="M0 0h17L0 17z" fill="#0a6bcb"/></svg>
</section>

<section class="abs services">
  <h2 class="abs services-title">OUR SERVICES</h2>
  <div class="abs svc-photo" style="left:82px;background:linear-gradient(160deg,#bdb8ae,#8a857c 60%,#c7c1b6)" role="img" aria-label="Modern living room with concrete fireplace and pendant lamp"></div>
  <div class="abs svc-photo" style="left:279px;background:linear-gradient(170deg,#f1efea,#cfd2d8 55%,#4b4f6e)" role="img" aria-label="Open plan office with rows of blue desk chairs"></div>
  <div class="abs svc-photo" style="left:475px;background:linear-gradient(170deg,#c9ccd2,#a7abb2 50%,#d8d8d6)" role="img" aria-label="Empty industrial warehouse with a scissor lift"></div>

  <div class="abs svc-card" style="left:92px">
    <div class="abs svc-icon-col"><svg width="18" height="16" viewBox="0 0 18 16" fill="none" stroke="#e31e2c" stroke-width="1.5"><path d="M1 8L9 1l8 7"/><path d="M3 7v8h12V7"/><rect x="7" y="9" width="4" height="6"/></svg></div>
    <div class="abs svc-name">Residential</div>
    <div class="abs svc-text">Indignation and dislike men who are so beguiled and our the charms moment.</div>
  </div>
  <div class="abs svc-card" style="left:289px">
    <div class="abs svc-icon-col"><svg width="18" height="16" viewBox="0 0 18 16" fill="none" stroke="#e31e2c" stroke-width="1.5"><path d="M1 5l2-4h12l2 4z"/><path d="M2 5v10h14V5"/><rect x="4" y="8" width="4" height="7"/><rect x="10" y="8" width="4" height="4"/></svg></div>
    <div class="abs svc-name">Commercial</div>
    <div class="abs svc-text">Righteous indignation work are so beguiled demoralized the blinded by desire.</div>
  </div>
  <div class="abs svc-card" style="left:485px">
    <div class="abs svc-icon-col"><svg width="18" height="16" viewBox="0 0 18 16" fill="#e31e2c"><rect x="1" y="4" width="5" height="12"/><rect x="12" y="4" width="5" height="12"/><rect x="6" y="9" width="6" height="7"/><rect x="2.5" y="0" width="2" height="4"/><rect x="13.5" y="0" width="2" height="4"/></svg></div>
    <div class="abs svc-name">Industries</div>
    <div class="abs svc-text">Our power of choice is and when nothing prevents work every pleasure interior.</div>
  </div>

  <div class="abs plus" style="left:215px"><svg width="11" height="11"><path d="M5.5 0v11M0 5.5h11" stroke="#fff" stroke-width="1.4"/></svg></div>
  <div class="abs plus" style="left:411px"><svg width="11" height="11"><path d="M5.5 0v11M0 5.5h11" stroke="#fff" stroke-width="1.4"/></svg></div>
  <div class="abs plus" style="left:608px"><svg width="11" height="11"><path d="M5.5 0v11M0 5.5h11" stroke="#fff" stroke-width="1.4"/></svg></div>
</section>

<section>
  <div class="abs clients-eyebrow">CORPORATE CLIENTS</div>
  <h2 class="abs clients-title"><b>MORE THAN</b> 2000 CLIENTS</h2>
  <div class="abs arrow-btn" style="left:605px"><svg width="12" height="7"><path d="M12 3.5H1M4 0.5L1 3.5l3 3" fill="none" stroke="#aaa"/></svg></div>
  <div class="abs arrow-btn" style="left:639px"><svg width="12" height="7"><path d="M0 3.5h11M8 0.5l3 3-3 3" fill="none" stroke="#aaa"/></svg></div>
  <div class="abs client" style="left:50px">Tidewell</div>
  <div class="abs client" style="left:156px">Norhaven</div>
  <div class="abs client" style="left:261px;font-size:11px">Quarrystone</div>
  <div class="abs client" style="left:367px">Lumencrest</div>
  <div class="abs client" style="left:473px">Oakform</div>
  <div class="abs client" style="left:579px">Tidewell</div>
</section>
</body>
</html>
```